Etikettendesign für Imkereiprodukt
Zielgruppe
Ich betreibe eine Imkerei nach ökologischen Gesichtspunkten und vertreibe alles rund um die Biene- Honig, Wachs, Met, Likör...
Aus Bienenwachs und reinem Leinöl stelle ich ein natürliches Holzwachs her. (Wachs stammt aus eigener Bio Imkerei, Leinöl wird in Deutschland hergestellt)
Mit dem Wachs werden unbehandelte Hölzer imprägniert, gegen Feuchtigkeit geschützt, das Wachs verleiht dem Holz einen matten Glanz
Für dieses Produkt benötige ich ein Etikett.
Aufgabenstellung
- rundes Etikett Durchmesser 85 mm
- Verwendung von eigenem Firmenlogo (Anhang) (Name der Imkerei auch 'Wabenritter')
- Verwendung von folgenden Textbausteinen:
'ausschließlich Leinöl und Bienenwachs'
'regional von Hand hergestellt'
'komplett ohne Lösungsmittel'
oder ähnlich
- Herstelleradresse
- Datei nach Druck-vorgaben

```html
<!DOCTYPE html>
<html lang="de">
<head>
<meta charset="utf-8">
<title>Holzwachs Etikett</title>
<link rel="stylesheet" href="https://fonts.googleapis.com/css2?family=Rubik+Dirt&family=Oswald:wght@600&family=Source+Sans+3:wght@400;700&display=swap">
<style>
  :root {
    --bg-gold: #b39d66;
    --label-black: #222222;
    --label-white: #ffffff;
    --accent-gold: #b89b5e;
    --text-light: #f2f2f2;
  }
  * { margin: 0; padding: 0; box-sizing: border-box; }
  html, body { width: 1200px; height: 1199px; overflow: hidden; }
  body {
    background: var(--bg-gold);
    position: relative;
    font-family: "Source Sans 3", sans-serif;
  }
  .label {
    position: absolute;
    left: 345px; top: 100px;
    width: 510px; height: 520px;
  }
  .label-shape { position: absolute; inset: 0; }
  .label-content {
    position: absolute; inset: 0;
    text-align: center;
  }
  .brand-mark {
    position: absolute; top: 95px; left: 0; right: 0;
    display: flex; justify-content: center; align-items: center; gap: 8px;
    color: var(--accent-gold);
    font-weight: 700; font-size: 22px;
  }
  .brand-mark .square {
    width: 14px; height: 14px; background: var(--accent-gold);
  }
  .product-title {
    position: absolute; top: 226px; left: 0; right: 0;
    font-family: "Rubik Dirt", sans-serif;
    font-weight: 400;
    font-size: 50px; letter-spacing: 2px;
    color: var(--label-white);
    line-height: 1;
  }
  .product-claim {
    position: absolute; top: 274px; left: 0; right: 0;
    font-family: "Oswald", sans-serif; font-weight: 600;
    font-size: 15.5px; letter-spacing: 2.2px;
    color: var(--accent-gold);
  }
  .product-facts {
    position: absolute; top: 309px; left: 0; right: 0;
    list-style: none;
    font-size: 17px; line-height: 23px;
    color: var(--text-light);
  }
  .maker {
    position: absolute; top: 390px; left: 0; right: 0;
    font-size: 13px; line-height: 18px;
    font-style: normal;
  }
  .maker-name { color: var(--text-light); font-weight: 700; }
  .maker-address, .maker-web { color: var(--accent-gold); }
  .maker-web { font-weight: 700; }
</style>
</head>
<body>
  <div class="label">
    <svg class="label-shape" viewBox="0 0 510 520" width="510" height="520" aria-hidden="true">
      <path d="M255 8 C 390 4 500 110 504 250 C 508 390 400 514 258 512 C 110 510 4 400 6 260 C 8 120 120 12 255 8 Z" fill="var(--label-white)"/>
      <path d="M255 22 C 380 20 488 118 490 252 C 492 385 392 498 258 498 C 120 498 20 395 22 260 C 24 125 128 24 255 22 Z" fill="var(--label-black)"/>
      <circle cx="256" cy="258" r="218" fill="none" stroke="var(--label-white)" stroke-width="1.5"/>
      <circle cx="256" cy="258" r="205" fill="none" stroke="var(--label-white)" stroke-width="1"/>
    </svg>
    <div class="label-content">
      <div class="brand-mark"><span class="square"></span><span>Wabenritter</span></div>
      <h1 class="product-title">HOLZWACHS</h1>
      <p class="product-claim">REGIONAL VON HAND HERGESTELLT</p>
      <ul class="product-facts">
        <li>· ausschließlich Leinöl und Bienenwachs</li>
        <li>· komplett ohne Lösungsmittel</li>
      </ul>
      <address class="maker">
        <div class="maker-name">Imkerei Wabenhüter</div>
        <div class="maker-address">Lindenweg 3, 54321 Waldheim</div>
        <div class="maker-web">www.wabenritter.com</div>
      </address>
    </div>
  </div>
</body>
</html>
```